"Got Radon?" Banner Ads

I need banner ads made for Pelvaro Banner Circuit campaign. There are 10 sizes of banners, so I need all 10 sizes. All of them can be similar in design and concept, but need to look good and the content must fill the space nicely.

The text on the ad is "Got Radon?" big/bold, and there should be a picture of a house with gas seeping into it from the ground. I have attached an example of an existing ad for reference.

These are the 10 sizes of banners that we need:
970x90
120x600
160x600
200x200
250x250
350x250
300x600
336x280
468x60
728x90

```html
<!DOCTYPE html>
<html lang="en">
<head>
<meta charset="utf-8">
<title>Got Radon? – Pelvaro Banner Circuit banner set</title>
<link rel="stylesheet" href="https://fonts.googleapis.com/css2?family=Montserrat:wght@700;800&family=Oswald:wght@500&display=swap">
<style>
  :root{
    --stage:#4a4a4a;
    --navy:#0b3f8f;
    --yellow:#ffec00;
    --white:#ffffff;
    --ink:#3d3a00;
    --sky:#cfe2f5;
    --grass:#3fae3a;
    --haze:#6fd05a;
  }
  html,body{margin:0;padding:0;overflow:hidden}
  body{width:1200px;height:1200px;background:var(--stage);position:relative}
  .banner{position:absolute;background:var(--navy);overflow:hidden;box-shadow:0 2px 5px rgba(0,0,0,.45)}
  .photo{position:absolute;inset:0;
    background:
      radial-gradient(ellipse at 55% 70%, rgba(111,208,90,.85) 0%, rgba(111,208,90,0) 55%),
      linear-gradient(180deg,var(--sky) 0%,#e6ecef 35%,#b9c7a8 50%,#7cc062 68%,var(--grass) 100%);}
  .photo.green-top{background:
      radial-gradient(ellipse at 50% 8%, rgba(80,190,70,.95) 0%, rgba(80,190,70,0) 45%),
      radial-gradient(ellipse at 55% 78%, rgba(111,208,90,.85) 0%, rgba(111,208,90,0) 55%),
      linear-gradient(180deg,#7fcf6a 0%,#dfeaf2 30%,#d6e2e8 50%,#8cc46e 70%,var(--grass) 100%);}
  .pill{position:absolute;top:6%;bottom:6%;border:2px solid var(--white);border-radius:40px 50% 50% 40px / 50%;overflow:hidden}
  .pill .photo{background:
      radial-gradient(ellipse at 40% 60%, rgba(111,208,90,.9) 0%, rgba(111,208,90,0) 60%),
      linear-gradient(90deg,#c9d8c4 0%,#8cc26c 40%,var(--grass) 100%);}
  .swoosh{position:absolute;inset:0;width:100%;height:100%}
  .swoosh .fill{fill:var(--navy)}
  .swoosh .edge{fill:none;stroke:var(--white);stroke-width:5;vector-effect:non-scaling-stroke}
  .headline{position:absolute;left:0;right:0;margin:0;text-align:center;white-space:nowrap;
    font-family:"Montserrat",sans-serif;font-weight:800;color:var(--yellow);line-height:1;
    text-shadow:0 0 2px var(--ink),1px 1px 2px rgba(0,0,0,.55)}
  .tagline{font-family:"Oswald",sans-serif;font-weight:500;color:var(--white);line-height:1;
    transform:scaleX(.82);transform-origin:center;white-space:nowrap;margin:0}
  .cta{display:inline-flex;align-items:center;justify-content:center;gap:.45em;background:var(--yellow);
    color:var(--navy);font-family:"Montserrat",sans-serif;font-weight:700;line-height:1;
    border:1px solid var(--white);border-radius:3px;white-space:nowrap;box-sizing:border-box}
  .cta svg{width:.9em;height:.9em}
  .cta svg path{fill:none;stroke:currentColor;stroke-width:3}
  .footer{position:absolute;left:0;right:0;display:flex;align-items:center;justify-content:center;text-align:center}
  .footer.stack{flex-direction:column}
  .side{position:absolute;top:0;bottom:0;display:flex;flex-direction:column;justify-content:center;align-items:center}
</style>
</head>
<body>

<!-- 160x600 skyscraper -->
<div class="banner" style="left:44px;top:105px;width:135px;height:509px">
  <div class="photo" role="img" aria-label="House with green radon gas rising from the lawn"></div>
  <svg class="swoosh" viewBox="0 0 100 100" preserveAspectRatio="none" aria-hidden="true">
    <path class="fill" d="M0,0 L100,0 L100,6 Q45,2 0,20 Z"/><path class="edge" d="M100,6 Q45,2 0,20"/>
    <path class="fill" d="M0,79 Q55,84 100,68 L100,100 L0,100 Z"/><path class="edge" d="M0,79 Q55,84 100,68"/>
  </svg>
  <p class="headline" style="top:166px;font-size:50px">GOT</p>
  <p class="headline" style="top:213px;font-size:27px">RADON</p>
  <p class="headline" style="top:248px;font-size:42px">?</p>
  <div class="footer stack" style="top:420px;gap:2px">
    <p class="tagline" style="font-size:22px">WE WILL</p>
    <p class="tagline" style="font-size:22px">GET RID OF IT !</p>
    <span class="cta" style="font-size:11px;width:107px;height:19px;margin-top:8px">CLICK HERE <svg viewBox="0 0 10 10"><path d="M3,1 L7,5 L3,9"/></svg></span>
  </div>
</div>

<!-- 120x600 skyscraper -->
<div class="banner" style="left:199px;top:105px;width:103px;height:509px">
  <div class="photo" role="img" aria-label="House with green radon gas rising from the lawn"></div>
  <svg class="swoosh" viewBox="0 0 100 100" preserveAspectRatio="none" aria-hidden="true">
    <path class="fill" d="M0,0 L100,0 L100,4 Q40,2 0,18 Z"/><path class="edge" d="M100,4 Q40,2 0,18"/>
    <path class="fill" d="M0,80 Q60,86 100,62 L100,100 L0,100 Z"/><path class="edge" d="M0,80 Q60,86 100,62"/>
  </svg>
  <p class="headline" style="top:187px;font-size:38px">GOT</p>
  <p class="headline" style="top:223px;font-size:21px">RADON</p>
  <p class="headline" style="top:250px;font-size:32px">?</p>
  <div class="footer stack" style="top:443px;gap:3px">
    <p class="tagline" style="font-size:17px">WE WILL</p>
    <p class="tagline" style="font-size:17px">GET RID OF IT !</p>
    <span class="cta" style="font-size:8px;width:80px;height:13px;margin-top:5px">CLICK HERE <svg viewBox="0 0 10 10"><path d="M3,1 L7,5 L3,9"/></svg></span>
  </div>
</div>

<!-- 300x600 half page -->
<div class="banner" style="left:332px;top:105px;width:254px;height:509px">
  <div class="photo green-top" role="img" aria-label="Brick house with green radon gas seeping up from the ground"></div>
  <svg class="swoosh" viewBox="0 0 100 100" preserveAspectRatio="none" aria-hidden="true">
    <path class="fill" d="M0,76 Q50,92 100,78 L100,100 L0,100 Z"/><path class="edge" d="M0,76 Q50,92 100,78"/>
  </svg>
  <p class="headline" style="top:88px;font-size:80px">GOT</p>
  <p class="headline" style="top:168px;font-size:47px">RADON</p>
  <p class="headline" style="top:222px;font-size:72px">?</p>
  <div class="footer stack" style="top:440px;gap:10px">
    <p class="tagline" style="font-size:28px">WE WILL GET RID OF IT !</p>
    <span class="cta" style="font-size:13px;width:112px;height:19px">CLICK HERE <svg viewBox="0 0 10 10"><path d="M3,1 L7,5 L3,9"/></svg></span>
  </div>
</div>

<!-- 468x60 banner -->
<div class="banner" style="left:614px;top:105px;width:330px;height:30px">
  <div class="pill" style="left:10px;width:240px;top:1px;bottom:1px">
    <div class="photo" role="img" aria-label="Row of houses with green radon gas"></div>
  </div>
  <p class="headline" style="top:7px;left:70px;right:auto;font-size:17px">GOT RADON?</p>
  <div class="side" style="left:254px;width:76px;gap:2px">
    <p class="tagline" style="font-size:7px">WE WILL GET RID OF IT !</p>
    <span class="cta" style="font-size:4px;width:42px;height:7px">CLICK HERE <svg viewBox="0 0 10 10"><path d="M3,1 L7,5 L3,9"/></svg></span>
  </div>
</div>

<!-- 970x90 leaderboard -->
<div class="banner" style="left:614px;top:164px;width:511px;height:65px">
  <div class="pill" style="left:22px;width:364px">
    <div class="photo" role="img" aria-label="Houses with green radon gas drifting across the lawn"></div>
  </div>
  <p class="headline" style="top:17px;left:122px;right:auto;font-size:31px">GOT RADON?</p>
  <div class="side" style="left:390px;width:121px;gap:6px">
    <p class="tagline" style="font-size:13px">WE WILL GET RID OF IT !</p>
    <span class="cta" style="font-size:7px;width:68px;height:12px">CLICK HERE <svg viewBox="0 0 10 10"><path d="M3,1 L7,5 L3,9"/></svg></span>
  </div>
</div>

<!-- 728x90 leaderboard -->
<div class="banner" style="left:614px;top:266px;width:511px;height:64px">
  <div class="pill" style="left:18px;width:390px">
    <div class="photo" role="img" aria-label="Houses with green radon gas drifting across the lawn"></div>
  </div>
  <p class="headline" style="top:18px;left:100px;right:auto;font-size:31px">GOT RADON?</p>
  <div class="side" style="left:410px;width:101px;gap:6px">
    <p class="tagline" style="font-size:12px">WE WILL GET RID OF IT !</p>
    <span class="cta" style="font-size:7px;width:66px;height:12px">CLICK HERE <svg viewBox="0 0 10 10"><path d="M3,1 L7,5 L3,9"/></svg></span>
  </div>
</div>

<!-- 250x250 square -->
<div class="banner" style="left:614px;top:359px;width:237px;height:235px">
  <div class="photo" role="img" aria-label="Brick house with green radon gas seeping from the ground"></div>
  <svg class="swoosh" viewBox="0 0 100 100" preserveAspectRatio="none" aria-hidden="true">
    <path class="fill" d="M0,76 Q50,88 100,80 L100,100 L0,100 Z"/><path class="edge" d="M0,76 Q50,88 100,80"/>
  </svg>
  <p class="headline" style="top:142px;font-size:27px">GOT RADON?</p>
  <div class="footer" style="top:207px;gap:8px">
    <p class="tagline" style="font-size:17px;transform-origin:right">WE WILL GET RID OF IT !</p>
    <span class="cta" style="font-size:7px;width:74px;height:13px">CLICK HERE <svg viewBox="0 0 10 10"><path d="M3,1 L7,5 L3,9"/></svg></span>
  </div>
</div>

<!-- 200x200-style square, larger slot -->
<div class="banner" style="left:870px;top:359px;width:294px;height:294px">
  <div class="photo" role="img" aria-label="Brick house with green radon gas seeping from the ground"></div>
  <svg class="swoosh" viewBox="0 0 100 100" preserveAspectRatio="none" aria-hidden="true">
    <path class="fill" d="M0,74 Q50,88 100,76 L100,100 L0,100 Z"/><path class="edge" d="M0,74 Q50,88 100,76"/>
  </svg>
  <p class="headline" style="top:179px;font-size:34px">GOT RADON?</p>
  <div class="footer" style="top:260px;gap:8px">
    <p class="tagline" style="font-size:22px;transform-origin:right">WE WILL GET RID OF IT !</p>
    <span class="cta" style="font-size:8px;width:90px;height:15px">CLICK HERE <svg viewBox="0 0 10 10"><path d="M3,1 L7,5 L3,9"/></svg></span>
  </div>
</div>

<!-- 336x280 rectangle -->
<div class="banner" style="left:44px;top:688px;width:475px;height:395px">
  <div class="photo" role="img" aria-label="Brick house under blue sky with green radon gas rising around it"></div>
  <svg class="swoosh" viewBox="0 0 100 100" preserveAspectRatio="none" aria-hidden="true">
    <path class="fill" d="M0,72 Q45,88 100,68 L100,100 L0,100 Z"/><path class="edge" d="M0,72 Q45,88 100,68"/>
  </svg>
  <p class="headline" style="top:220px;font-size:51px">GOT RADON?</p>
  <div class="footer" style="top:344px;gap:12px">
    <p class="tagline" style="font-size:32px;transform-origin:right">WE WILL GET RID OF IT !</p>
    <span class="cta" style="font-size:14px;width:140px;height:26px">CLICK HERE <svg viewBox="0 0 10 10"><path d="M3,1 L7,5 L3,9"/></svg></span>
  </div>
</div>

<!-- 350x250 rectangle -->
<div class="banner" style="left:586px;top:688px;width:494px;height:354px">
  <div class="photo" role="img" aria-label="Two-storey house with trees behind and green radon gas seeping from the lawn"
       style="background:radial-gradient(ellipse at 50% 75%, rgba(111,208,90,.9) 0%, rgba(111,208,90,0) 55%),linear-gradient(180deg,#3f6a35 0%,#9aa3a6 30%,#e2e2dc 48%,#8cc46e 68%,var(--grass) 100%)"></div>
  <svg class="swoosh" viewBox="0 0 100 100" preserveAspectRatio="none" aria-hidden="true">
    <path class="fill" d="M0,74 Q50,88 100,70 L100,100 L0,100 Z"/><path class="edge" d="M0,74 Q50,88 100,70"/>
  </svg>
  <p class="headline" style="top:188px;font-size:53px">GOT RADON?</p>
  <div class="footer" style="top:304px;gap:14px">
    <p class="tagline" style="font-size:32px;transform-origin:right">WE WILL GET RID OF IT !</p>
    <span class="cta" style="font-size:14px;width:140px;height:26px">CLICK HERE <svg viewBox="0 0 10 10"><path d="M3,1 L7,5 L3,9"/></svg></span>
  </div>
</div>

</body>
</html>
```